Revamp Of Landing Page For an Automated AI Voice Agents Agency

here is my current landing page https://app.brightfunnelstudio.example/v2/preview/KXWQPmR4hLsDnTfYvJcA?notrack=true

Please use all my current content and imagery of ai agents in your new design. Make it easy to ready, easy to navigate and easy to understand

I am looking for a SLEEK shiny polished looking website. I like Dark themed sites but am open to see light themed sites too so please dont be shy.

The site should have an Ai Voice Agent Theme about it. Maybe look and feel of futureistic but simple and not intimidating to the average person...

Here are a couple website designs I like for reference:
https://q4t.example/
https://ai-bots.mervinholt.example/
https://chatvexo.example/ai-agents

Target Market(s)

b2b

Industry/Entity Type

AI Voice Agents

Coding

Coded - Design and coding required

Font styles to use
Other font styles liked:
• open

Requirements
Must have
• all elements and content and images used in existing design.
Nice to have
• open
Should not have
• open

```html
<!DOCTYPE html>
<html lang="en">
<head>
<meta charset="utf-8">
<title>Vocalyne — AI Voice Agents</title>
<link rel="stylesheet" href="https://fonts.googleapis.com/css2?family=Plus+Jakarta+Sans:ital,wght@0,400;0,500;0,600;0,700;0,800;1,600;1,700&display=swap">
<style>
:root{
  --ink:#14122a;
  --muted:#4a4860;
  --purple:#6a4ce8;
  --purple-2:#7d55f2;
  --blue:#4f5ae6;
  --navy:#0f0b3a;
  --navy-2:#16104a;
  --card-dark:#1a1450;
  --line-dark:#3a3180;
  --white:#ffffff;
  --soft:#f3efff;
}
*{box-sizing:border-box;margin:0;padding:0}
html,body{width:1200px;height:5268px;overflow:hidden}
body{font-family:"Plus Jakarta Sans",Arial,sans-serif;color:var(--ink);background:var(--white);position:relative}
section,footer{position:absolute;left:0;width:1200px}
.abs{position:absolute}
.btn{position:absolute;display:flex;align-items:center;justify-content:center;color:#fff;font-weight:700;font-size:18px;border-radius:6px;background:linear-gradient(90deg,var(--blue),var(--purple-2));text-decoration:none}
.accent{color:var(--purple)}
.accent-light{color:#8b6cff}
.dark{background:radial-gradient(ellipse at 50% 0%,#241a6b 0%,var(--navy) 60%);color:#fff}
.photo{position:absolute;border-radius:10px;overflow:hidden}
.cta-note{position:absolute;left:0;width:1200px;text-align:center;font-style:italic;font-weight:700;font-size:14.5px;line-height:20.5px;color:#e8e6ff}
.sec-title{position:absolute;left:0;width:1200px;text-align:center;font-weight:700;font-size:40px;line-height:49px}

/* hero */
.hero{top:0;height:654px;background:linear-gradient(180deg,#ffffff 0%,#f6f2ff 40%,#ffffff 100%)}
.brand{left:41px;top:50px;display:flex;align-items:center;gap:8px;font-weight:700;font-size:27px;letter-spacing:1px;color:var(--ink)}
.brand .dot{width:14px;height:14px;border-radius:50%;background:var(--purple)}
.hero h1{left:41px;top:160px;font-size:42px;line-height:48px;font-weight:700}
.checks{left:41px;top:278px;width:520px;display:grid;grid-template-columns:190px 260px;row-gap:12px;font-size:16px;color:var(--ink)}
.checks span{display:flex;align-items:center;gap:8px}
.hero-note{left:41px;top:496px;width:440px;font-size:14.5px;line-height:19px;color:var(--ink)}

/* workforce */
.workforce{top:654px;height:812px}
.agent-card{position:absolute;top:191px;height:300px;border:1px solid var(--line-dark);background:var(--card-dark);border-radius:10px}
.agent-card .photo{top:15px;left:15px;width:188px;height:268px}
.agent-card h3{position:absolute;left:302px;top:58px;font-size:25px;font-weight:600;color:#fff}
.agent-icon{position:absolute;left:232px;top:50px;width:62px;height:62px;border-radius:50%}
.agent-card p{position:absolute;left:232px;font-size:14px;line-height:20px;color:#d8d6f0}
.progress{left:41px;top:522px;width:1116px;height:7px;border-radius:4px;background:#2a2270}
.progress i{display:block;width:447px;height:7px;border-radius:4px;background:linear-gradient(90deg,var(--blue),var(--purple-2))}

/* install */
.install{top:1466px;height:534px;background:#fff}
.install h2{left:84px;top:120px;font-size:40px;line-height:46px;font-weight:700}
.install h4{left:84px;top:232px;font-size:24px;font-weight:600;color:var(--purple)}
.install p{left:84px;top:276px;width:450px;font-size:16px;line-height:21.5px;color:var(--ink)}

/* why */
.why{top:2000px;height:616px}
.feature{position:absolute;top:147px;height:195px;border:1px solid var(--line-dark);border-radius:8px;background:var(--card-dark);text-align:center}
.feature svg{position:absolute;left:50%;top:20px;transform:translateX(-50%)}
.feature h3{position:absolute;left:0;right:0;font-size:23px;font-weight:600;line-height:28px}
.feature p{position:absolute;left:10px;right:10px;font-size:14.5px;line-height:19px;color:#cfcdea}

/* promise */
.promise{top:2616px;height:615px;background:#fff}
.promise h2{left:564px;top:172px;font-size:38px;font-weight:700}
.promise-box{position:absolute;left:564px;border:1px solid #c9c4e6;border-radius:4px;display:flex;align-items:center;gap:12px;padding-left:18px}
.promise-box strong{font-size:23px;font-weight:600}
.promise-box small{display:block;font-size:17px;line-height:21px;color:var(--ink);margin-top:2px}

/* reviews */
.reviews{top:3231px;height:638px}
.review{position:absolute;top:256px;width:351px;height:264px;border:1px solid var(--line-dark);border-radius:10px;background:var(--card-dark);padding:22px 16px}
.review .stars{display:flex;gap:4px;margin-bottom:10px}
.review p{font-size:14.5px;line-height:20px;color:#dcdaf2}
.review p b{color:#fff}
.review .who{position:absolute;left:16px;bottom:18px;display:flex;align-items:center;gap:10px}
.avatar{width:64px;height:64px;border-radius:50%}
.who strong{display:block;font-size:15px;font-weight:700}
.who span{font-size:12.5px;color:#cfcdea}
.dots{left:0;top:3779px;width:1200px;display:flex;justify-content:center;gap:8px}

/* faq */
.faq{top:3869px;height:685px;background:#fff}
.faq-item{position:absolute;left:297px;width:607px;border:2px solid #b9a9ff;border-radius:6px;text-align:center;padding-top:22px}
.faq-item h3{font-size:24px;font-weight:600;margin-bottom:10px}
.faq-item p{font-size:17px;line-height:23px;color:var(--ink)}

/* final cta + footer */
.final{top:4554px;height:714px;background:linear-gradient(180deg,#3a2a8f 0%,#1a1358 35%,var(--navy) 100%);color:#fff}
.foot-col{position:absolute;top:481px;font-size:13.5px;line-height:21px;color:#c9c7e6}
.foot-col h5{font-size:14.5px;font-weight:700;color:#fff;margin-bottom:6px}
.rule{left:0;top:620px;width:1200px;height:1px;background:#2d2570}
.copy{left:84px;top:652px;font-size:13.5px;color:#c9c7e6}
.socials{left:1016px;top:646px;display:flex;gap:14px}
.socials i{width:24px;height:24px;border-radius:50%;background:#8f8db0;display:block}
</style>
</head>
<body>

<section class="hero">
  <div class="abs brand"><span class="dot"></span>VOCALYNE</div>
  <a class="btn" style="left:867px;top:37px;width:290px;height:61px" href="#">Get An Instant Free Demo</a>
  <h1 class="abs">AI Voice Agents That Work<br><span class="accent">24 Hours 7 Days A Week!</span></h1>
  <div class="abs checks">
    <span><svg width="18" height="18" viewBox="0 0 18 18"><circle cx="9" cy="9" r="9" fill="#6a4ce8"/><path d="M5 9.2l2.6 2.6L13 6.4" stroke="#fff" stroke-width="2" fill="none"/></svg>Answering Calls</span>
    <span><svg width="18" height="18" viewBox="0 0 18 18"><circle cx="9" cy="9" r="9" fill="#6a4ce8"/><path d="M5 9.2l2.6 2.6L13 6.4" stroke="#fff" stroke-width="2" fill="none"/></svg>Send Emails &amp; Text Messages</span>
    <span><svg width="18" height="18" viewBox="0 0 18 18"><circle cx="9" cy="9" r="9" fill="#6a4ce8"/><path d="M5 9.2l2.6 2.6L13 6.4" stroke="#fff" stroke-width="2" fill="none"/></svg>Book Appointments</span>
    <span><svg width="18" height="18" viewBox="0 0 18 18"><circle cx="9" cy="9" r="9" fill="#6a4ce8"/><path d="M5 9.2l2.6 2.6L13 6.4" stroke="#fff" stroke-width="2" fill="none"/></svg>Follow Up Reminders</span>
    <span><svg width="18" height="18" viewBox="0 0 18 18"><circle cx="9" cy="9" r="9" fill="#6a4ce8"/><path d="M5 9.2l2.6 2.6L13 6.4" stroke="#fff" stroke-width="2" fill="none"/></svg>Transfer Calls &amp; More</span>
  </div>
  <a class="btn" style="left:41px;top:401px;width:292px;height:64px" href="#">Get An Instant Free Demo</a>
  <p class="abs hero-note">We'll create a custom AI agent for your business at no cost.<br>Click the button above — your new AI agent will call you<br>in just a couple of minutes. Experience the magic and<br>prepare to be impressed!</p>
  <div class="photo" style="left:611px;top:168px;width:546px;height:402px;background:linear-gradient(135deg,#c9d6e6,#8a9bb3 55%,#e6e9ef)" role="img" aria-label="Two AI voice agents in white robotic suits with headsets working at laptops"></div>
</section>

<section class="workforce dark">
  <div class="sec-title" style="top:75px">Meet Your New<br><span class="accent-light">AI-Powered Workforce</span></div>
  <div class="agent-card" style="left:41px;width:552px">
    <div class="photo" role="img" aria-label="AI receptionist agent wearing a headset" style="background:linear-gradient(160deg,#3b7fa8,#a9c8de 60%,#e7eef4)"></div>
    <svg class="agent-icon" viewBox="0 0 62 62"><circle cx="31" cy="31" r="31" fill="#2cb58f"/><path d="M19 34v-4a12 12 0 0124 0v4" stroke="#fff" stroke-width="3" fill="none"/><rect x="16" y="32" width="7" height="10" rx="2" fill="#fff"/><rect x="39" y="32" width="7" height="10" rx="2" fill="#fff"/></svg>
    <h3>AI Receptionist</h3>
    <p style="top:130px;width:300px;font-weight:700;color:#fff">Takes overflow and after-hours calls, or handles calls 24/7 &amp; transfers to the appropriate department.</p>
    <p style="top:196px;width:300px">Lena handles all your calls 24/7. She can also be set to only manage overflow or after-hours calls. Lena sends emails, SMS messages, and even books appointments during calls.</p>
  </div>
  <div class="agent-card" style="left:611px;width:546px">
    <div class="photo" role="img" aria-label="AI sales agent with a headset at a desk by city windows" style="background:linear-gradient(160deg,#8fa6bd,#dfe6ee 55%,#5f6f82)"></div>
    <svg class="agent-icon" style="top:52px" viewBox="0 0 62 62"><circle cx="31" cy="31" r="31" fill="#2d6ee8"/><circle cx="31" cy="31" r="17" stroke="#fff" stroke-width="2.5" fill="none"/><text x="31" y="38" text-anchor="middle" font-size="20" font-weight="700" fill="#fff" font-family="Plus Jakarta Sans,sans-serif">$</text></svg>
    <h3 style="top:60px">Ai Sales Agent</h3>
    <p style="top:132px;width:300px">Owen will take your inbound sales calls. Will give all detailed information to the customer, answer questions in a normal conversational tone and can book sales appointments or transfer hot prospects to a human to close the sale.</p>
  </div>
  <div class="abs progress"><i></i></div>
  <a class="btn" style="left:368px;top:595px;width:464px;height:62px" href="#">Get An Instant Free Demo</a>
  <p class="cta-note" style="top:683px">We Will Create An Ai Agent Customized For Your Business At No Cost.<br>Simply Click The Button Above And Your Very Own Ai Agent Will Be Calling You In<br>Just A Couple Minutes. Experience The Magic And Get Ready To Be Very Impressed!</p>
</section>

<section class="install">
  <h2 class="abs">Install The <span class="accent">Power Of AI</span><br>For Your Business</h2>
  <h4 class="abs">Your Wish Is Their Command</h4>
  <p class="abs">Welcome your newest employees — AI Voice Agents who never call in sick, never complain, and never take a break. From handling inbound calls to sending emails, booking appointments, and following up with leads, your AI team works around the clock to save you time and money.</p>
  <div class="photo" style="left:636px;top:82px;width:481px;height:368px;background:linear-gradient(135deg,#3f8aa0,#cfe0e4 50%,#8fb2bd)" role="img" aria-label="Two smiling AI agents in robotic suits with headsets in an office"></div>
</section>

<section class="why dark">
  <div class="sec-title" style="top:75px">Why Businesses Love <span class="accent-light">AI Voice Agents</span></div>
  <div class="feature" style="left:41px;width:249px">
    <svg width="54" height="54" viewBox="0 0 54 54" fill="none" stroke="#8b6cff" stroke-width="2.5"><path d="M20 34l-6-6 18-18c4-4 10-4 12-4 0 2 0 8-4 12L22 36z"/><path d="M14 28l-6 2 8-10h8M26 40l-2 6 10-8v-8"/><circle cx="35" cy="19" r="3"/></svg>
    <h3 style="top:92px">Trained in Seconds</h3>
    <p style="top:128px">Learns Your Entire Website<br>In Seconds</p>
  </div>
  <div class="feature" style="left:319px;width:260px">
    <svg width="54" height="54" viewBox="0 0 54 54" fill="none" stroke="#8b6cff" stroke-width="2.5"><circle cx="27" cy="27" r="22"/><path d="M5 27h44M27 5c8 8 8 36 0 44M27 5c-8 8-8 36 0 44"/></svg>
    <h3 style="top:102px">Worldwide</h3>
    <p style="top:138px">Works Anywhere In The Globe</p>
  </div>
  <div class="feature" style="left:607px;width:238px">
    <svg width="54" height="54" viewBox="0 0 54 54" fill="none" stroke="#8b6cff" stroke-width="2.5"><circle cx="27" cy="17" r="9"/><path d="M12 48c0-10 7-16 15-16s15 6 15 16z"/><path d="M17 17a10 10 0 0120 0"/></svg>
    <h3 style="top:92px">User-friendly</h3>
    <p style="top:128px">Your Ai Agents Sound As If<br>They're Real Humans</p>
  </div>
  <div class="feature" style="left:873px;width:284px">
    <svg width="54" height="54" viewBox="0 0 54 54" fill="none" stroke="#8b6cff" stroke-width="2.5"><path d="M30 6L16 30h11l-4 18 16-26H28z"/><path d="M8 12l6 4M46 12l-6 4M6 36h6M42 36h6"/></svg>
    <h3 style="top:78px">Lightning-Fast<br>Responses</h3>
    <p style="top:142px">Instant answers, no coffee,<br>bathroom or lunch breaks needed</p>
  </div>
  <a class="btn" style="left:368px;top:399px;width:464px;height:62px" href="#">Get An Instant Free Demo</a>
  <p class="cta-note" style="top:487px">We Will Create An Ai Agent Customized For Your Business At No Cost.<br>Simply Click The Button Above And Your Very Own Ai Agent Will Be Calling You In<br>Just A Couple Minutes. Experience The Magic And Get Ready To Be Very Impressed!</p>
</section>

<section class="promise">
  <div class="photo" style="left:168px;top:83px;width:337px;height:446px;background:linear-gradient(135deg,#4e8ea0,#d6e3e6 55%,#9fb7bd)" role="img" aria-label="Smiling AI agent in a robotic suit with a headset"></div>
  <h2 class="abs">Our <span class="accent">Promise</span> To You</h2>
  <div class="promise-box" style="top:237px;width:469px;height:80px">
    <svg width="48" height="48" viewBox="0 0 48 48"><circle cx="24" cy="24" r="21" fill="none" stroke="#6a4ce8" stroke-width="2" stroke-dasharray="4 3"/><circle cx="24" cy="24" r="15" fill="none" stroke="#6a4ce8" stroke-width="2"/><text x="24" y="31" text-anchor="middle" font-size="19" font-weight="700" fill="#6a4ce8" font-family="Plus Jakarta Sans,sans-serif">$</text></svg>
    <strong>14-day money-back guarantee</strong>
  </div>
  <div class="promise-box" style="top:335px;width:381px;height:106px">
    <svg width="44" height="48" viewBox="0 0 44 48" fill="none" stroke="#6a4ce8" stroke-width="2"><circle cx="22" cy="16" r="9"/><path d="M11 16a11 11 0 0122 0M33 18v4a4 4 0 01-4 4h-4"/><path d="M6 46c0-10 7-15 16-15s16 5 16 15z"/></svg>
    <div><strong>24/7 Customer Support</strong><small>Often praised for our friendly<br>&amp; helpful support team</small></div>
  </div>
</section>

<section class="reviews dark">
  <div class="sec-title" style="top:76px">After Our Customers Have A Conversation<br>With Their New Ai Voice Agent<br><span class="accent-light">They Give Us 5 Stars!</span></div>
  <div class="review" style="left:41px">
    <div class="stars"><svg width="88" height="16" viewBox="0 0 88 16" fill="#8b6cff"><path id="st" d="M8 0l2.4 5 5.6.6-4.2 3.8 1.2 5.6L8 12.2 3 15l1.2-5.6L0 5.6 5.6 5z"/><use href="#st" x="18"/><use href="#st" x="36"/><use href="#st" x="54"/><use href="#st" x="72"/></svg></div>
    <p>Before using this, I was drowning in missed calls and follow-ups. Now, everything just runs. Clients are getting booked, messages go out automatically — <b>it feels like my business finally has structure.</b></p>
    <div class="who"><div class="avatar" role="img" aria-label="Customer portrait" style="background:linear-gradient(135deg,#4a5fd0,#b5c1f0)"></div><div><strong>Dean Harlow</strong><span>CEO, Fernway Solutions</span></div></div>
  </div>
  <div class="review" style="left:423px">
    <div class="stars"><svg width="88" height="16" viewBox="0 0 88 16" fill="#8b6cff"><use href="#st"/><use href="#st" x="18"/><use href="#st" x="36"/><use href="#st" x="54"/><use href="#st" x="72"/></svg></div>
    <p><b>It's like I suddenly got a super-reliable assistant who never forgets a thing.</b> My calendar stays full, no one slips through the cracks, and I've got more time to actually grow the business.</p>
    <div class="who"><div class="avatar" role="img" aria-label="Customer portrait" style="background:linear-gradient(135deg,#d9c08a,#6c7ad6)"></div><div><strong>Nora Castell</strong><span>CEO of Brookline Strategies</span></div></div>
  </div>
  <div class="review" style="left:806px">
    <div class="stars"><svg width="88" height="16" viewBox="0 0 88 16" fill="#8b6cff"><use href="#st"/><use href="#st" x="18"/><use href="#st" x="36"/><use href="#st" x="54"/><use href="#st" x="72"/></svg></div>
    <p>What used to take three people and constant oversight now happens on autopilot. Calls get handled, leads get qualified, and I can focus on closing deals. <b>Best decision I've made all year.</b></p>
    <div class="who"><div class="avatar" role="img" aria-label="Customer portrait" style="background:linear-gradient(135deg,#e0903a,#6c4ad6)"></div><div><strong>Marcus Okafor</strong><span>CEO of Okafor Consulting Firm</span></div></div>
  </div>
</section>
<div class="abs dots"><svg width="66" height="12" viewBox="0 0 66 12"><circle cx="6" cy="6" r="5" fill="none" stroke="#fff" stroke-width="1.5"/><circle cx="24" cy="6" r="5" fill="#8e8bb0"/><circle cx="42" cy="6" r="5" fill="#8e8bb0"/><circle cx="60" cy="6" r="5" fill="#8e8bb0"/></svg></div>

<section class="faq">
  <div class="sec-title" style="top:74px;color:var(--ink)">Do You Have Questions?</div>
  <div class="faq-item" style="top:147px;height:148px"><h3>What exactly are the AI Voice Agents?</h3><p>AI Voice Agents are specialized human sounding bots, having<br>smart and masterful conversations and each is expertly trained<br>in seconds for a specific business function.</p></div>
  <div class="faq-item" style="top:323px;height:127px"><h3>How will these AI Voice Agents benefit</h3><p>Ai Voice Agents Answer Calls, Book Appts, Send Emails,<br>Text Messages, Follow Up Reminders &amp; More For You 24/7!</p></div>
  <div class="faq-item" style="top:477px;height:124px"><h3>Are they easy to use?</h3><p>We provide a done for you service. We create your<br>AI Voice Agent and launch it within days!</p></div>
</section>

<footer class="final">
  <div class="sec-title" style="top:78px">These AI Agents Can Help Your Business<br>Tremendously. Imagine The Possibilities.</div>
  <a class="btn" style="left:368px;top:217px;width:464px;height:62px" href="#">Get An Instant Free Demo</a>
  <p class="cta-note" style="top:305px">We Will Create An Ai Agent Customized For Your Business At No Cost.<br>Simply Click The Button Above And Your Very Own Ai Agent Will Be Calling You In<br>Just A Couple Minutes. Experience The Magic And Get Ready To Be Very Impressed!</p>
  <div class="foot-col" style="left:84px;width:320px"><h5>*14-Day Money Back Guarantee Terms:</h5>If you use the ai agents and you're not happy. Then you can contact us in the first 14 days for a full refund.</div>
  <div class="foot-col" style="left:499px"><h5>Legal</h5>Privacy<br>Terms and Conditions<br>Earnings &amp; Product Disclaimer</div>
  <div class="foot-col" style="left:812px;width:330px"><h5>Contact</h5>Do you have questions about Vocalyne? Please email info@vocalyne.example.</div>
  <div class="abs rule"></div>
  <div class="abs copy">© 2025 Vocalyne. All Rights Reserved.</div>
  <div class="abs socials"><i></i><i></i><i></i></div>
</footer>

</body>
</html>
```